label design for oral care product

Kindly invite you to design bottle label (114 mm*40 mm) for our product, a kind of oral care product. The GEL is different from our previous cleanser product, as the pic we uploaded for demonstration. The color of frosted glass bottle is dark green, but the cap is white. You could download the pic of bottle among the uploaded files. The logo file and label content description are attached too. Please check them. Our product is made from many kinds of natural plant extracts, which includes herb and fruit. I wish the label would make our product look high-end and reliable. And it would be better if you could give some advice on paper material and special requirements for printing, related to your design. I value the texture of label too, because I think that stands for the quality of products. No color limitation for the use of our logo.
Target Market(s)
20-40 female, who value oral health.
Colors
Designer to choose colors to be used in the design.
Look and feel
Each slider illustrates characteristics of the customer's brand and the style your logo design should communicate.

```html
<!DOCTYPE html>
<html lang="en">
<head>
<meta charset="utf-8">
<title>Aligner Gel – Label</title>
<link rel="stylesheet" href="https://fonts.googleapis.com/css2?family=PT+Sans+Narrow:wght@400;700&family=Montserrat:wght@300;500&display=swap">
<style>
  :root {
    --bg: #e9e9ea;
    --olive-dark: #33341b;
    --olive-side: #454b22;
    --olive-side-light: #5a6030;
    --gold: #c9a04e;
    --gold-light: #e8c878;
    --paper: #ececec;
  }
  * { box-sizing: border-box; margin: 0; padding: 0; }
  html, body { width: 1200px; height: 1200px; overflow: hidden; }
  body { background: var(--bg); position: relative; font-family: "PT Sans Narrow", sans-serif; }

  .label {
    position: absolute; left: 40px; top: 403px;
    width: 1120px; height: 394px;
    display: flex;
    box-shadow: 0 6px 24px rgba(0,0,0,.18);
  }
  .panel { position: relative; height: 100%; overflow: hidden; }
  .panel--side {
    width: 373px;
    background: linear-gradient(100deg, var(--olive-side) 0%, var(--olive-side-light) 55%, var(--olive-side) 100%);
    color: var(--gold);
    font-size: 16.5px; line-height: 1.28;
    padding: 42px 28px 0 32px;
  }
  .panel--side strong { color: var(--gold-light); font-weight: 700; }
  .panel--side p + p { margin-top: 16px; }
  .panel--front { width: 374px; background: var(--olive-dark); }

  .front-curve { position: absolute; inset: 0; }
  .brand {
    position: absolute; left: 200px; top: 58px;
    display: flex; align-items: center; gap: 8px;
    font-family: "Montserrat", sans-serif; font-weight: 500;
    font-size: 30px; line-height: 1; color: var(--gold);
  }
  .brand-dot { width: 12px; height: 12px; border-radius: 50%; background: var(--gold); }

  .front-title {
    position: absolute; left: 0; top: 394px;
    width: 394px; height: 200px;
    transform: rotate(-90deg); transform-origin: top left;
    padding: 18px 0 0 14px;
    font-family: "Montserrat", sans-serif; color: var(--gold);
  }
  .product-name { font-size: 44px; line-height: 44px; letter-spacing: 1px; white-space: nowrap; }
  .product-name .name-bold { font-weight: 500; }
  .product-name .name-light { font-weight: 300; }
  .tagline { font-size: 19px; font-weight: 300; line-height: 21px; margin-top: 6px; letter-spacing: .5px; }
  .claim { font-family: "PT Sans Narrow", sans-serif; font-size: 11.5px; line-height: 13px; margin-top: 6px; }
  .volume { font-family: "Montserrat", sans-serif; font-weight: 300; font-size: 16px; margin-top: 14px; }
</style>
</head>
<body>
  <div class="label">
    <section class="panel panel--side panel--info">
      <p>Lorem <strong>ipsum dolor</strong> sit amet, consectetur adipiscing elit Proin <strong>non</strong> risus sollicitudin leo luctus placerat. Nulla <strong>eu tellus</strong> at leo blandit rutrum. <strong>Pellentesque</strong> sodales leo sed dui placerat, venenatis tincidunt <strong>metus</strong> lacinia. Maecenas <strong>auctor</strong> odio facilisis turpis vehicula eleifend. Sed <strong>aliquet</strong> tellus eu hendrerit mollis.</p>
      <p><strong>Directions:</strong> <strong>Drop</strong> on the teeth directly after brushing. Or, put <strong>into clear</strong> aligners before wearing again. No <strong>need to rinse</strong> your mouth with water.</p>
    </section>

    <section class="panel panel--front">
      <svg class="front-curve" width="374" height="394" viewBox="0 0 374 394" aria-hidden="true">
        <path d="M100 0 C100 170 230 272 374 274 L374 0 Z" fill="var(--paper)"/>
      </svg>
      <div class="brand"><span class="brand-name">Petal Pure</span><span class="brand-dot"></span></div>
      <div class="front-title">
        <h1 class="product-name"><span class="name-bold">ALIGNER</span><span class="name-light">GEL</span></h1>
        <p class="tagline">IMMUNE SUPPORT<br>FOR ORAL HEALTH</p>
        <p class="claim">the Solution to Maintain<br>Dental Hygiene and Strengthen Gums</p>
        <p class="volume">30 ml / 1 fl oz</p>
      </div>
    </section>

    <section class="panel panel--side panel--contents">
      <p>Maecenas <strong>ultricies felis vitae eros</strong> pellentesque. Nunc id <strong>ante eget metus</strong> fermentum <strong>dictum et.</strong> Proin id <strong>velit gravida,</strong> dictum ante <strong>eget, gravida.</strong> Proin lacinia <strong>sem nec est sodales, nec.</strong> Proin congue <strong>arcu eu pharetra facilisis.</strong> Nulla aliquet <strong>diam porttitor scelerisque varius.</strong> Maecenas <strong>sed urna quis tortor lobortis.</strong></p>
      <p style="margin-top:40px"><strong>Contains:</strong> a proprietary blend of natural <strong>plant extract</strong> including Angelica, Radix Rehmanniae, <strong>Coptis,</strong> Honeysuckle, Echinacea, Sage, <strong>Chamomile,</strong> Acerola cherry.</p>
      <p style="margin-top:30px">Made in Taiwan</p>
    </section>
  </div>
</body>
</html>
```